Start-up Cleaning Business Needs Professional Business Cards

Marta's Butler Cleaning, LLC, is a start-up business based in the Northern Virginia suburbs of Washington, DC. MBC provides cleaning and housekeeping services for homes and offices. We have three core values:

1. We are personal. We value knowing and being known by our customers and each other. If you want nameless, faceless service, you should choose another provider. We put "personal" at the front of the list, because it is most important to us; the design we choose will convey this value.

2. Like a hotel concierge, we are professional in attitude, posture, communication and processes.

3. Like a hotel concierge, we solve problems with a can-do attitude and never make excuses.

Our uniforms are khaki pants with pink polo shirts.

Our logo is attached. There are other symbols, not represented in our logo, that may convey our values well, such as a top hat and bow tie, magnifying glass, desk bell, etc.

Please include fields for an individual's name and title, office phone number, mobile phone number, email address and website address (www.martasbutlercleaning.example).

Standard U.S. size: 2" x 3.5"
Updates

I should have mentioned that the purpose of all our advertising - business cards included - is to motivate potential customers to call or email to arrange a free in-home estimate.

```html
<!DOCTYPE html>
<html lang="en">
<head>
<meta charset="utf-8">
<title>Marta's Butler Cleaning, LLC – Business Card</title>
<link rel="stylesheet" href="https://fonts.googleapis.com/css2?family=Arimo:wght@400;700&display=swap">
<style>
  :root {
    --backdrop: #ebe6de;
    --card: #ffffff;
    --pink: #e8419a;
    --ink: #1e1e1e;
    --ink-soft: #3a3a3a;
    --brand-ink: #454545;
    --band-grey: #cfcfcf;
    --band-light: #f2f2f2;
    --figure-tone: #f6eef1;
  }
  * { box-sizing: border-box; margin: 0; padding: 0; }
  html, body {
    width: 1050px; height: 1200px; overflow: hidden;
    background: var(--backdrop);
    font-family: "Arimo", Arial, sans-serif;
  }
  .canvas { position: relative; width: 1050px; height: 1200px; }
  .card {
    position: absolute; left: 58px; width: 922px; height: 525px;
    background: var(--card);
    box-shadow: 0 4px 14px rgba(0,0,0,.18);
    overflow: hidden;
  }
  .card--front { top: 38px; }
  .card--back { top: 612px; height: 551px; }

  .name-band { position: absolute; inset: 0; width: 922px; height: 525px; }

  .holder {
    position: absolute; left: 24px; top: 108px;
    font-size: 38px; font-weight: 700; color: var(--ink); letter-spacing: .2px;
  }
  .holder__title { font-size: 25px; font-weight: 400; }

  .call-to-action {
    position: absolute; left: 600px; top: 132px; width: 300px;
    text-align: center; color: var(--ink-soft); font-size: 28px; line-height: 38px;
  }
  .call-to-action strong { color: var(--pink); font-size: 30px; }

  .contacts { position: absolute; left: 24px; top: 228px; list-style: none; }
  .contacts li {
    display: flex; align-items: center; gap: 10px;
    height: 44px; font-size: 23px; color: var(--ink-soft);
  }
  .contacts svg { width: 20px; height: 20px; flex: none; }

  .brand-name {
    position: absolute; font-weight: 400; color: var(--brand-ink); white-space: nowrap;
  }
  .card--front .brand-name { left: 22px; top: 440px; font-size: 38px; }
  .card--back .brand-name {
    left: 0; right: 0; top: 228px; text-align: center; font-size: 50px;
  }

  .mascot-area {
    position: absolute; left: 318px; top: 36px; width: 290px; height: 440px;
    background: linear-gradient(180deg, var(--figure-tone), #fbf7f8);
    border-radius: 40px;
  }
</style>
</head>
<body>
<div class="canvas">

  <section class="card card--front">
    <svg class="name-band" viewBox="0 0 527 300" preserveAspectRatio="none" aria-hidden="true">
      <defs>
        <linearGradient id="bandFill" x1="0" x2="1" y1="0" y2="0">
          <stop offset="0.38" stop-color="#ffffff"/>
          <stop offset="0.55" stop-color="var(--band-grey)"/>
          <stop offset="0.62" stop-color="#e4e4e4"/>
          <stop offset="1" stop-color="var(--band-light)"/>
        </linearGradient>
      </defs>
      <path d="M0,35 L180,35 C225,35 230,65 275,65 L527,65 L527,152 L420,152 C370,152 350,108 300,108 L0,108 Z" fill="url(#bandFill)"/>
      <path d="M0,35 L180,35 C225,35 230,65 275,65 L527,65" fill="none" stroke="var(--pink)" stroke-width="2"/>
      <path d="M0,108 L300,108 C350,108 370,152 420,152 L527,152" fill="none" stroke="var(--pink)" stroke-width="2"/>
    </svg>

    <h1 class="holder">INDIVID NAME, <span class="holder__title">TITLE</span></h1>

    <p class="call-to-action"><strong>Call or email</strong><br>to arrange a free in<br>home estimate</p>

    <ul class="contacts">
      <li>
        <svg viewBox="0 0 20 20" aria-hidden="true"><circle cx="10" cy="10" r="8.5" fill="none" stroke="var(--pink)" stroke-width="1.8"/><path d="M7 5.5l2 2-1 1.5c.7 1.4 1.6 2.3 3 3l1.5-1 2 2-1.3 1.5C9.5 14 6 10.5 5.5 6.8z" fill="var(--pink)"/></svg>
        (123) 456-7890
      </li>
      <li>
        <svg viewBox="0 0 20 20" aria-hidden="true"><rect x="5.5" y="1.5" width="9" height="17" rx="2" fill="var(--pink)"/><rect x="7" y="4" width="6" height="9" fill="#fff"/><circle cx="10" cy="15.5" r="1" fill="#fff"/></svg>
        (123) 456-7890
      </li>
      <li>
        <svg viewBox="0 0 20 20" aria-hidden="true"><rect x="2" y="5" width="16" height="11" rx="1.5" fill="var(--pink)"/><path d="M2.5 5.8L10 11l7.5-5.2" fill="none" stroke="#fff" stroke-width="1.4"/></svg>
        info@martasbutlercleaning.example
      </li>
      <li>
        <svg viewBox="0 0 20 20" aria-hidden="true"><circle cx="10" cy="10" r="8.5" fill="var(--pink)"/><g fill="none" stroke="#fff" stroke-width="1.1"><ellipse cx="10" cy="10" rx="3.6" ry="8.5"/><path d="M1.5 10h17M3 5.8h14M3 14.2h14"/></g></svg>
        www.martasbutlercleaning.example
      </li>
    </ul>

    <p class="brand-name">Marta's Butler Cleaning, LLC</p>
  </section>

  <section class="card card--back">
    <div class="mascot-area" role="img" aria-label="Faint illustration of a housekeeper in a pink uniform mopping the floor"></div>
    <p class="brand-name">Marta's Butler Cleaning, LLC</p>
  </section>

</div>
</body>
</html>
```